Clearview Property Inspections

Property Inspection ( pre-purchase building inspections, swimming pool inspection, pest inspection , maintenance)

Industry/Entity Type

Building

Contact Information for Business Card

Tomas Varnell
info@clearviewinspect-demo.com.au
0412 867 219

ClearView Property Inspections
www.clearviewinspect-demo.com.au

on the back

Property Inspections
Property Maintenance

Inspect Well....Live Easy

```html
<!DOCTYPE html>
<html lang="en">
<head>
<meta charset="utf-8">
<title>ClearView Property Inspections – Business Card</title>
<link rel="stylesheet" href="https://fonts.googleapis.com/css2?family=Lato:wght@400;700&display=swap">
<style>
  :root {
    --page: #e9e7e4;
    --charcoal: #2e2e30;
    --charcoal-light: #3b3b3e;
    --paper: #ffffff;
    --paper-shade: #cfcfd1;
    --brand-blue: #2e4c86;
    --ink: #1c1c1e;
    --text-light: #e8e8ea;
  }
  * { margin: 0; padding: 0; box-sizing: border-box; }
  html, body {
    width: 1200px; height: 1200px; overflow: hidden;
    background: var(--page);
    font-family: "Lato", "Helvetica Neue", Arial, sans-serif;
  }
  .stage {
    position: relative; width: 1200px; height: 1200px;
    display: flex; flex-direction: column; align-items: center; justify-content: center; gap: 40px;
  }
  .card {
    position: relative; width: 900px; height: 514px; overflow: hidden;
    box-shadow: 0 10px 28px rgba(0,0,0,0.25);
  }

  /* Front */
  .card-front { background: var(--charcoal); }
  .front-header {
    position: absolute; left: 0; top: 0; width: 100%; height: 200px;
    background: radial-gradient(ellipse at 70% 20%, var(--paper) 0%, #f1f1f2 45%, var(--paper-shade) 100%);
  }
  .brand {
    position: absolute; left: 52px; top: 122px;
    display: flex; align-items: center; gap: 14px;
  }
  .brand-dot { width: 22px; height: 22px; border-radius: 50%; background: var(--brand-blue); }
  .brand-name { font-size: 34px; font-weight: 700; color: var(--ink); letter-spacing: 0.5px; }

  .contact-list {
    position: absolute; left: 72px; top: 262px; list-style: none;
    display: flex; flex-direction: column; gap: 20px;
  }
  .contact-item { display: flex; align-items: center; gap: 22px; color: var(--text-light); font-size: 19px; letter-spacing: 0.3px; }
  .contact-icon { width: 20px; height: 20px; flex: none; }

  .front-rule { position: absolute; left: 0; top: 403px; width: 100%; height: 5px; background: var(--paper); }
  .front-band {
    position: absolute; left: 0; top: 420px; width: 100%; height: 94px;
    background: var(--brand-blue);
    display: flex; align-items: center; padding-left: 240px;
  }
  .front-band-url { color: var(--text-light); font-size: 19px; letter-spacing: 0.3px; }

  /* Back */
  .card-back { background: linear-gradient(160deg, var(--charcoal-light) 0%, var(--charcoal) 60%, #252527 100%); }
  .back-band {
    position: absolute; left: 0; top: 118px; width: 100%; height: 56px;
    background: var(--brand-blue);
    display: flex; align-items: center; justify-content: center;
  }
  .back-slogan { color: var(--text-light); font-size: 25px; letter-spacing: 0.3px; white-space: nowrap; }
</style>
</head>
<body>
<main class="stage">

  <section class="card card-front" aria-label="Business card front">
    <div class="front-header">
      <div class="brand">
        <span class="brand-dot"></span>
        <span class="brand-name">ClearView Property Inspections</span>
      </div>
    </div>

    <ul class="contact-list">
      <li class="contact-item">
        <svg class="contact-icon" viewBox="0 0 24 24" aria-hidden="true">
          <path fill="#e8e8ea" d="M6.6 10.8a15.1 15.1 0 0 0 6.6 6.6l2.2-2.2c.3-.3.7-.4 1-.2 1.1.4 2.3.6 3.6.6.6 0 1 .4 1 1V20c0 .6-.4 1-1 1A17 17 0 0 1 3 4c0-.6.4-1 1-1h3.5c.6 0 1 .4 1 1 0 1.3.2 2.5.6 3.6.1.3 0 .7-.2 1z"/>
        </svg>
        <span>0412 867 219</span>
      </li>
      <li class="contact-item">
        <svg class="contact-icon" viewBox="0 0 24 24" aria-hidden="true">
          <rect x="2" y="5" width="20" height="14" fill="none" stroke="#e8e8ea" stroke-width="1.8"/>
          <path d="M2 5l10 8 10-8" fill="none" stroke="#e8e8ea" stroke-width="1.8"/>
        </svg>
        <span>Tomas Varnell info@clearviewinspect-demo.com.au</span>
      </li>
      <li class="contact-item">
        <svg class="contact-icon" viewBox="0 0 24 24" aria-hidden="true">
          <circle cx="12" cy="12" r="10" fill="#e8e8ea"/>
          <path d="M2 12h20M12 2c3 3 3 17 0 20M12 2c-3 3-3 17 0 20" fill="none" stroke="#2e2e30" stroke-width="1.4"/>
        </svg>
        <span>www.clearviewinspect-demo.com.au</span>
      </li>
    </ul>

    <div class="front-rule"></div>
    <div class="front-band">
      <span class="front-band-url">www.clearviewinspect-demo.com.au</span>
    </div>
  </section>

  <section class="card card-back" aria-label="Business card back">
    <div class="back-band">
      <span class="back-slogan">Property Inspections Property Maintenance Inspect Well....Live Easy</span>
    </div>
  </section>

</main>
</body>
</html>
```